Front Cover Page and Back Cover for Biography Book

Create a book front cover page and back cover for the biography book called Beyond the Tide: The Long Road of Pham Quoc Lanh
Blurb/Summary:
Step into the extraordinary life of Pham Quoc Lanh in Beyond the Tide: The Long Road of Pham Quoc Lanh, a gripping memoir of resilience, determination, and triumph. Born in Quang Ngai, Vietnam, in 1938, Lanh grew up amid the unrelenting challenges of famine, war, and poverty. Yet, his unshakable thirst for education and self-improvement became the foundation of a journey that would defy every expectation.
From studying under flickering oil lamps in hidden village schools during the resistance against French colonial rule to enduring the hardships of the Vietnam War, Lanh’s story is set against the dramatic backdrop of a nation in turmoil. Despite familial and societal obstacles, his passion for knowledge drove him to excel academically and chart a future far beyond the limitations of his humble beginnings.
As a Navy officer, Lanh balanced the rigours of military life with an entrepreneurial spirit that saw him transform his circumstances. Whether selling ice cream, expanding a fleet of fishing boats, or salvaging a sunken ship to create a thriving business, his ingenuity and drive turned adversity into opportunity. Along the way, he navigated personal sacrifices, betrayal, and daring escapes as Vietnam descended into chaos, all while keeping his family at the heart of his efforts.
Through the lens of Lanh’s incredible life, Beyond the Tide highlights the power of education, perseverance, and community in overcoming the impossible. This memoir is not just a story of survival but a testament to human strength, offering readers an inspiring tale of hope, legacy, and the relentless pursuit of a better life. Perfect for those seeking an uplifting narrative with historical and emotional depth, this is a book that will stay with you long after the final page.
Please find the full book attached.
Photos of lanh can be found here in the photo album: https://albums.pictoria-share.example/Xk7RmqTz2wLpYc9Vn

```html
<!DOCTYPE html>
<html lang="en">
<head>
<meta charset="utf-8">
<title>Beyond the Tide – Cover Spread</title>
<link href="https://fonts.googleapis.com/css2?family=Bebas+Neue&family=Great+Vibes&family=Montserrat:wght@300;400;700&family=Raleway:wght@300&display=swap" rel="stylesheet">
<style>
  :root {
    --bg: #d9d8d3;
    --back-grey: #8c8c8c;
    --spine-grey: #a3a3a3;
    --band-dark: #4a4a4a;
    --band-light: #a9a9a9;
    --photo-light: #9a9a9a;
    --photo-mid: #6e6e6e;
    --photo-dark: #3f3f3f;
    --gold: #e0b843;
    --white: #f4f4f4;
  }
  * { margin: 0; padding: 0; box-sizing: border-box; }
  html, body { width: 1200px; height: 1041px; overflow: hidden; background: var(--bg); }
  .spread {
    position: absolute; left: 50px; top: 183px;
    width: 1100px; height: 675px; display: flex;
    box-shadow: 0 12px 30px rgba(0,0,0,.18);
  }
  .back-cover { position: relative; width: 520px; height: 100%; background: var(--back-grey); }
  .back-cover .blurb {
    position: absolute; left: 60px; right: 60px; top: 420px;
    font: 400 12.5px/1.5 "Montserrat", sans-serif; color: var(--white); text-align: center;
  }
  .band-dark { position: absolute; left: 0; right: 0; top: 585px; height: 36px; background: var(--band-dark); }
  .band-light { position: absolute; left: 0; right: 0; top: 621px; height: 22px; background: var(--band-light); }
  .credits {
    position: absolute; left: 0; right: 0; top: 585px; height: 36px; line-height: 36px;
    text-align: center; font: 700 11px "Montserrat", sans-serif; letter-spacing: 1.2px; color: var(--gold);
  }
  .spine { position: relative; width: 60px; height: 100%; background: var(--spine-grey); }
  .front-cover { position: relative; width: 520px; height: 100%; overflow: hidden; }
  .portrait {
    position: absolute; inset: 0;
    background:
      radial-gradient(ellipse 45% 38% at 42% 32%, var(--photo-light), transparent 70%),
      radial-gradient(ellipse 70% 40% at 45% 85%, #b8b8b8, transparent 75%),
      linear-gradient(180deg, var(--photo-mid) 0%, var(--photo-dark) 100%);
  }
  .byline {
    position: absolute; top: 30px; right: 14px;
    writing-mode: vertical-rl; display: flex; flex-direction: row; gap: 2px;
  }
  .byline-script { font: 400 19px "Great Vibes", cursive; color: var(--white); }
  .byline-name { font: 300 26px "Raleway", sans-serif; letter-spacing: 1.5px; color: var(--white); }
  .title {
    position: absolute; left: 0; right: 0; top: 495px; text-align: center;
    font: 400 70px/1 "Bebas Neue", sans-serif; color: var(--gold);
    text-shadow: 3px 4px 6px rgba(0,0,0,.55);
  }
  .subtitle-band {
    position: absolute; left: 0; right: 0; top: 600px; height: 36px; line-height: 36px;
    background: rgba(40,40,40,.75); text-align: center;
    font: 700 13px "Montserrat", sans-serif; letter-spacing: 1.5px; color: var(--gold);
  }
</style>
</head>
<body>
  <div class="spread">
    <section class="back-cover">
      <p class="blurb">Lorem ipsum dolor sit amet, consectetuer adipiscing elit, sed diam nonummy nibh euismod tincidunt ut laoreet dolore magna aliquam erat volutpat, e molestie consequat, vel illum dolore eu feugiat nulla facilisis at vero eros et accumsan et iusto odio dignissim qui blandit praesent luptatum</p>
      <div class="band-dark"></div>
      <div class="band-light"></div>
      <p class="credits">ALL CREDITS AND COPYWRITES GOES TO THE WRITTER@</p>
    </section>
    <section class="spine">
      <div class="band-dark"></div>
      <div class="band-light"></div>
    </section>
    <section class="front-cover">
      <div class="portrait" role="img" aria-label="Black and white portrait photograph of Pham Quoc Lanh in a striped collared shirt"></div>
      <div class="byline">
        <span class="byline-script">The Authorised Biography of</span>
        <span class="byline-name">PHAM QUOC LANH</span>
      </div>
      <h1 class="title">BEYOND THE TIDE</h1>
      <p class="subtitle-band">THE LONG ROAD OF PHAM QUOC LANH</p>
    </section>
  </div>
</body>
</html>
```